Toronto's Airline, based in Downtown looking for a whole new look and feel.

SkyVarn is looking for a new look in our website. We are an airline based at Corwen Haddle Airfield in Toronto. You can view our current website/services at www.skyvarn.example. We are expanding our services and look forward to a very sleek and modernized website. Please view the different pages on our website, we also need to add several new plane types as we have expanded and the website is not current. Would also be interesting to have a news feed or update feed through a widget which would be easy to use and update. we will also be implementing 2 third party programs called tolvo and quendrix on the website, both are tour based and airline based sales and management functions.

Target Market(s)

Commuters, travel, tourism, dates, general public

Industry/Entity Type

Airline

Coding

Coded - Design and coding required

Number of Pages Required

5+ page

Font styles to use
Other font styles liked:
• Toronto subway font would be nice

Requirements
Must have
• A modern feel, easy to use, our booking function is currently a bit confusing which we will be working on. Content can be taken from our current website www.skyvarn.example
Nice to have
• work with out theme colours of blue and light grey

```html
<!DOCTYPE html>
<html lang="en">
<head>
<meta charset="utf-8">
<title>SkyVarn – Toronto's Airline</title>
<link href="https://fonts.googleapis.com/css2?family=Lato:wght@400;700&family=Open+Sans:ital,wght@0,400;0,600;0,700;1,400&display=swap" rel="stylesheet">
<style>
:root{
  --blue:#2f63c4;
  --blue-deep:#1f4fa8;
  --blue-band:#3a68b9;
  --grey-light:#e6e6e6;
  --grey-btn:#d0d0d0;
  --text:#222;
  --muted:#555;
  --footer:#353535;
  --footer-bottom:#2d2d2d;
  --white:#fff;
}
*{box-sizing:border-box;margin:0;padding:0}
html,body{width:1200px;height:2390px;overflow:hidden}
body{position:relative;background:var(--white);font-family:"Open Sans",Arial,sans-serif;color:var(--text)}
.abs{position:absolute}

/* header */
.site-header{position:absolute;left:0;top:0;width:1200px;height:104px;background:var(--white);border-top:4px solid var(--blue)}
.brand{position:absolute;left:86px;top:24px;display:flex;align-items:center;gap:14px}
.brand-dot{width:50px;height:50px;border-radius:50%;border:3px solid #7a7a7a}
.brand-name{font-family:"Lato",Arial,sans-serif;font-weight:700;font-size:40px;color:var(--blue);letter-spacing:1px}
.main-nav a{position:absolute;top:0;height:100px;line-height:100px;font-size:13px;color:#333;text-decoration:none;text-transform:uppercase}
.main-nav a.active{background:var(--blue);color:var(--white);padding:0 14px}
.social-dot{position:absolute;top:36px;width:26px;height:26px;border-radius:50%;background:#111}

/* hero */
.hero{position:absolute;left:0;top:104px;width:1200px;height:530px;
  background:linear-gradient(180deg,#6d6a66 0%,#a28670 30%,#e19a4b 48%,#8b7767 58%,#9a9690 68%,#6f6c6a 100%)}
.hero-title{position:absolute;left:86px;top:340px;font-family:"Lato",Arial,sans-serif;font-size:40px;color:var(--white);letter-spacing:.5px}
.hero-sub{position:absolute;left:92px;top:390px;width:360px;font-family:"Lato",Arial,sans-serif;font-size:19px;line-height:28px;color:var(--white)}
.btn-blue{position:absolute;background:var(--blue);color:var(--white);font-size:16px;text-align:center;text-transform:uppercase}

/* welcome */
.welcome-title{position:absolute;left:86px;top:700px;display:flex;align-items:flex-end;gap:12px;font-family:"Lato",Arial,sans-serif}
.welcome-title .lead{font-size:30px;color:#111}
.welcome-title .name{font-size:44px;font-weight:700;color:var(--blue);line-height:44px}
.divider{position:absolute;height:1px;background:#bbb}
.divider-mark{position:absolute;width:26px;height:26px;border-radius:50%;border:2px solid #777;background:var(--white)}
.welcome-copy{position:absolute;left:90px;top:806px;width:420px;text-align:center;font-size:13.5px;line-height:24px;color:var(--muted)}
.video{position:absolute;left:563px;top:698px;width:550px;height:324px;background:#0a0a0a}
.video-frame{position:absolute;left:0;top:0;width:550px;height:300px;background:linear-gradient(180deg,#1f2a33 0%,#31414d 55%,#1c252c 100%)}
.video-caption{position:absolute;left:0;top:132px;width:550px;text-align:center;font-size:24px;color:rgba(255,255,255,.8)}
.video-bar{position:absolute;left:0;bottom:0;width:550px;height:24px;background:#111}

/* services */
.services{position:absolute;left:0;top:1088px;width:1200px;height:599px;
  background:linear-gradient(180deg,#4d7bc7 0%,#3a68b9 55%,#2f5dae 100%)}
.services-title{position:absolute;left:0;top:50px;width:1200px;text-align:center;font-size:34px;color:var(--white);letter-spacing:2px}
.service{position:absolute;top:168px;width:380px;text-align:center;color:var(--white)}
.service-photo{width:232px;height:232px;margin:0 auto;border-radius:50%;border:3px solid var(--white)}
.service h3{font-weight:400;font-size:32px;margin-top:-12px;text-transform:uppercase}
.service p{font-size:13.5px;line-height:28px;margin-top:4px;height:92px}
.btn-grey{display:inline-block;width:140px;height:38px;line-height:38px;background:var(--grey-btn);color:#333;font-size:15px;text-transform:uppercase;border:1px solid #aaa}

/* testimonials */
.testimonial-photo{position:absolute;left:111px;top:1765px;width:302px;height:193px;background:linear-gradient(180deg,#8fbce6 0%,#cfe3f2 50%,#bdbdbb 70%,#8d8d8b 100%)}
.testimonial-title{position:absolute;left:455px;top:1780px;font-size:27px;color:#111}
.arrow-btn{position:absolute;top:1790px;width:30px;height:30px;border-radius:50%;border:2px solid #111}
.quote{position:absolute;left:455px;top:1843px;width:625px;font-style:italic;font-size:13.5px;line-height:24px;color:#555;text-indent:50px}
.quote-mark{position:absolute;font-family:Georgia,serif;font-size:90px;color:#ccc;line-height:1}

/* footer */
.site-footer{position:absolute;left:0;top:2018px;width:1200px;height:296px;background:var(--footer);color:#eee}
.footer-bottom{position:absolute;left:0;top:2314px;width:1200px;height:76px;background:var(--footer-bottom);border-top:1px solid #4a4a4a}
.footer-heading{position:absolute;font-family:"Lato",Arial,sans-serif;font-weight:700;font-size:17px;color:var(--white);text-transform:uppercase}
.contact-line{position:absolute;left:118px;font-size:13px;line-height:21px;color:#eee}
.quick-links{position:absolute;left:495px;top:2093px;width:270px;list-style:none}
.quick-links li{height:36px;line-height:36px;border-bottom:1px solid #4c4c4c;font-size:13.5px;padding-left:24px;position:relative;color:#eee}
.quick-links li::before{content:"";position:absolute;left:3px;top:16px;width:5px;height:5px;border-radius:50%;background:#888}
.subscribe{position:absolute;left:845px;top:2210px;width:270px;height:42px;border:1px solid #777;background:#2b2b2b}
.subscribe span{position:absolute;left:10px;top:12px;font-size:11px;color:#999}
.subscribe b{position:absolute;right:3px;top:3px;width:75px;height:34px;line-height:34px;background:var(--blue);color:var(--white);font-size:11px;text-align:center;font-weight:600}
</style>
</head>
<body>

<header class="site-header">
  <div class="brand"><span class="brand-dot"></span><span class="brand-name">SkyVarn</span></div>
  <nav class="main-nav">
    <a class="active" href="#" style="left:422px">Home</a>
    <a href="#" style="left:506px">Flights</a>
    <a href="#" style="left:588px">Charter &amp; Fleet</a>
    <a href="#" style="left:727px">Packages</a>
    <a href="#" style="left:824px">Gallery</a>
    <a href="#" style="left:908px">Contact</a>
    <a href="#" style="left:1000px">FAQ</a>
  </nav>
  <span class="social-dot" style="left:1046px"></span>
  <span class="social-dot" style="left:1086px"></span>
</header>

<section class="hero" role="img" aria-label="Twin-engine turboprop aircraft parked on a runway apron at sunset">
  <h1 class="hero-title">TORONTO'S AIRLINE</h1>
  <p class="hero-sub">We are an airline based at Corwen Haddle Airfield in Toronto.</p>
  <a class="btn-blue" style="left:90px;top:460px;width:132px;height:40px;line-height:40px;font-size:15px">Book Now!</a>
</section>

<section class="welcome">
  <h2 class="welcome-title"><span class="lead">WELCOME TO</span><span class="name">SkyVarn</span></h2>
  <span class="divider" style="left:128px;top:774px;width:140px"></span>
  <span class="divider" style="left:300px;top:774px;width:140px"></span>
  <span class="divider-mark" style="left:271px;top:761px"></span>
  <p class="welcome-copy">Toronto's top aerial experiences.<br>Photography | Flightseeing | Day Trips | Travel<br>Lorem Ipsum is simply dummy text of the printing and typesetting industry. Lorem Ipsum has been the industry's standard dummy text ever since the 1500s, when an unknown printer took a galley of type and scrambled it.</p>
  <a class="btn-blue" style="left:174px;top:983px;width:249px;height:40px;line-height:40px">Click here to book now!</a>

  <div class="video">
    <div class="video-frame" role="img" aria-label="View of the Toronto skyline from an aircraft window"></div>
    <p class="video-caption">Tired of your daily commute to Toronto?</p>
    <svg class="abs" style="left:240px;top:115px" width="70" height="70" viewBox="0 0 70 70">
      <circle cx="35" cy="35" r="32" fill="none" stroke="#fff" stroke-width="4"/>
      <path d="M27 20 L50 35 L27 50 Z" fill="#fff"/>
    </svg>
    <div class="video-bar">
      <svg width="550" height="24" viewBox="0 0 550 24">
        <path d="M6 7 L14 12 L6 17 Z" fill="#fff"/>
        <text x="22" y="16" font-size="8" fill="#ccc" font-family="Open Sans, sans-serif">00:00</text>
        <rect x="50" y="9" width="420" height="6" fill="#555"/>
        <rect x="50" y="9" width="5" height="6" fill="#ddd"/>
        <text x="480" y="16" font-size="8" fill="#ccc" font-family="Open Sans, sans-serif">01:56</text>
        <path d="M510 10 h3 l4 -3 v10 l-4 -3 h-3 Z" fill="#fff"/>
        <rect x="530" y="8" width="8" height="8" fill="none" stroke="#fff" stroke-width="1.5"/>
      </svg>
    </div>
  </div>
</section>

<section class="services" role="img" aria-label="Blue-tinted aerial view of downtown Toronto behind the services">
  <h2 class="services-title">SERVICES</h2>
  <span class="divider" style="left:444px;top:109px;width:137px;background:#dde6f5"></span>
  <span class="divider" style="left:619px;top:109px;width:137px;background:#dde6f5"></span>
  <span class="divider-mark" style="left:587px;top:96px;border-color:#fff;background:transparent"></span>

  <div class="service" style="left:16px">
    <div class="service-photo" role="img" aria-label="Aerial view of forested islands in a lake" style="background:linear-gradient(180deg,#b8cde0 0%,#6f8fa3 45%,#3f5f4a 70%,#5c7e8e 100%)"></div>
    <h3>Flights</h3>
    <p>LOOKING FOR SOMETHING NEW AND EXCITING IN TORONTO?<br>SKYVARN..</p>
    <span class="btn-grey">Learn More</span>
  </div>
  <div class="service" style="left:404px">
    <div class="service-photo" role="img" aria-label="Private aircraft on the apron with the city skyline behind" style="background:linear-gradient(180deg,#9ec3e8 0%,#c8d6e2 45%,#a9a49a 65%,#7f7b74 100%)"></div>
    <h3>Private Charter</h3>
    <p>COMPARABLE TO AIRLINE PRICES.<br>YOU'LL BE SURPRISED HOW AFFORDABLE IT REALLY IS.</p>
    <span class="btn-grey">Learn More</span>
  </div>
  <div class="service" style="left:794px">
    <div class="service-photo" role="img" aria-label="Runway stretching toward the Toronto skyline" style="background:linear-gradient(180deg,#c9d8e6 0%,#dfe3e2 45%,#8c8f6c 65%,#5f6a3f 100%)"></div>
    <h3>Gallery</h3>
    <p>Top aerial experiences.<br>Photography | Flightseeing | Day Trips | Travel</p>
    <span class="btn-grey">Learn More</span>
  </div>
</section>

<section class="testimonials">
  <svg class="abs" style="left:85px;top:1740px" width="200" height="175" viewBox="0 0 200 175">
    <path d="M0 0 H200 L26 175 V140 H0 Z" fill="var(--blue)"/>
  </svg>
  <div class="testimonial-photo" role="img" aria-label="Passengers walking from a private jet on the tarmac"></div>
  <h2 class="testimonial-title">WHAT VISITORS SAY</h2>
  <svg class="arrow-btn" style="left:1018px" viewBox="0 0 26 26"><path d="M15 7 L9 13 L15 19" fill="none" stroke="#111" stroke-width="2"/></svg>
  <svg class="arrow-btn" style="left:1055px" viewBox="0 0 26 26"><path d="M11 7 L17 13 L11 19" fill="none" stroke="#111" stroke-width="2"/></svg>
  <span class="quote-mark" style="left:450px;top:1818px">&ldquo;</span>
  <p class="quote">Lorem Ipsum is simply dummy text of the printing and typesetting industry. Lorem Ipsum has been the industry's standard dummy text ever since the 1500s. when an unknown printer took a galley of type and scrambled it to make a type specimen book.</p>
  <span class="quote-mark" style="left:838px;top:1890px">&rdquo;</span>
</section>

<footer class="site-footer">
  <h4 class="footer-heading" style="left:88px;top:44px">Contact Us</h4>
  <svg class="abs" style="left:88px;top:90px" width="12" height="16" viewBox="0 0 12 16"><path d="M6 0 A6 6 0 0 1 12 6 C12 10 6 16 6 16 C6 16 0 10 0 6 A6 6 0 0 1 6 0 Z" fill="#888"/><circle cx="6" cy="6" r="2" fill="#353535"/></svg>
  <p class="contact-line" style="top:84px">Corwen Haddle Airfield<br>Hangar 9, Suite 210, Toronto, Ontario<br>M0X 2B7</p>
  <svg class="abs" style="left:88px;top:175px" width="14" height="14" viewBox="0 0 14 14"><path d="M3 0 L5 4 L3.5 5.5 C4.5 7.5 6.5 9.5 8.5 10.5 L10 9 L14 11 L12.5 14 C6 13 1 8 0 1.5 Z" fill="#888"/></svg>
  <p class="contact-line" style="top:171px">+1 800 555 0142</p>
  <svg class="abs" style="left:88px;top:217px" width="16" height="11" viewBox="0 0 16 11"><rect width="16" height="11" fill="#888"/><path d="M0 0 L8 6 L16 0" fill="none" stroke="#353535" stroke-width="1.4"/></svg>
  <p class="contact-line" style="top:212px">info@skyvarn.example</p>

  <h4 class="footer-heading" style="left:492px;top:44px">Quick Links</h4>
  <ul class="quick-links" style="top:2093px;position:fixed"></ul>

  <h4 class="footer-heading" style="right:85px;top:44px">Stay Connected</h4>
  <span class="abs" style="left:1042px;top:92px;width:30px;height:30px;border-radius:50%;background:var(--blue)"></span>
  <span class="abs" style="left:1083px;top:92px;width:30px;height:30px;border-radius:50%;background:#d9427a"></span>
  <h4 class="footer-heading" style="right:85px;top:156px;font-size:14px">Subscribe to our news letter</h4>
</footer>
<ul class="quick-links">
  <li>FLIGHTS</li>
  <li>CHARTER &amp; FLEET</li>
  <li>PACKAGES</li>
  <li>GALLERY</li>
  <li>CONTACT</li>
</ul>
<div class="subscribe"><span>Enter Your Email Address</span><b>SUBSCRIBE</b></div>

<div class="footer-bottom">
  <svg class="abs" style="left:585px;top:0" width="30" height="10" viewBox="0 0 30 10"><path d="M0 0 L15 9 L30 0 Z" fill="#4a4a4a"/></svg>
  <p class="abs" style="left:85px;top:28px;font-size:12.5px;color:#999">&copy; 2017 <b style="color:#eee">SkyVarn</b> . All rights reserved.</p>
  <svg class="abs" style="left:1079px;top:17px" width="40" height="40" viewBox="0 0 40 40"><rect width="40" height="40" fill="#555"/><path d="M12 24 L20 16 L28 24" fill="none" stroke="#fff" stroke-width="2.5"/></svg>
</div>

</body>
</html>
```